Morvane Aesthetics Skin Care Flyer

8 1/2" x 11" three-folded brochure that will have a front panel which will show our Morvane Aesthetics logo and state that this is a Facial Menu. It might have our phone number on it and "call for appointment". The left inside flap will provide information about what we do and about the importance of facials and the rest will list services and pricing.
Updates

Brisquet Salon & Spa will not have a logo featured but it is important to show their address. Morvane Aesthetics has a newly designed logo but I am not sure how to upload it at this time. I do have a Vector file of our logo and hope to figure out the best way to make it available to all.Thank you. Added Sunday, April 26, 2015

```html
<!DOCTYPE html>
<html lang="en">
<head>
<meta charset="utf-8">
<title>Morvane Aesthetics Skin Care</title>
<link rel="stylesheet" href="https://fonts.googleapis.com/css2?family=Parisienne&family=Montserrat:wght@600;700&display=swap">
<style>
  :root {
    --gold: #d4a229;
    --white: #ffffff;
  }
  html, body {
    margin: 0;
    padding: 0;
    overflow: hidden;
    background: var(--white);
  }
  .flyer {
    position: relative;
    width: 1200px;
    height: 927px;
    overflow: hidden;
    display: flex;
  }
  .panel-back {
    width: 426px;
    height: 100%;
    background: var(--white);
    position: relative;
  }
  .panel-front {
    flex: 1;
    height: 100%;
    background: var(--gold);
    position: relative;
  }
  .brand {
    position: absolute;
    left: 0;
    right: 0;
    display: flex;
    flex-direction: column;
    align-items: center;
  }
  .panel-back .brand { top: 340px; }
  .panel-front .brand { top: 310px; }
  .brand-dot {
    width: 84px;
    height: 84px;
    border-radius: 50%;
    margin-bottom: 22px;
  }
  .panel-back .brand-dot { background: var(--gold); }
  .panel-front .brand-dot { background: var(--white); }
  .brand-name {
    font-family: "Parisienne", cursive;
    font-weight: 400;
    font-size: 44px;
    line-height: 1;
    margin: 0;
    white-space: nowrap;
  }
  .panel-back .brand-name { color: var(--gold); font-size: 40px; }
  .panel-front .brand-name { color: var(--white); }
  .call-to-action {
    position: absolute;
    top: 640px;
    left: 0;
    right: 0;
    text-align: center;
    font-family: "Parisienne", cursive;
    font-weight: 400;
    font-size: 64px;
    line-height: 1;
    color: var(--white);
    margin: 0;
  }
  .phone {
    position: absolute;
    top: 756px;
    left: 0;
    right: 0;
    text-align: center;
    font-family: "Montserrat", sans-serif;
    font-weight: 700;
    font-size: 22px;
    letter-spacing: 0.5px;
    color: var(--white);
    margin: 0;
  }
</style>
</head>
<body>
  <main class="flyer">
    <section class="panel-back">
      <div class="brand">
        <div class="brand-dot"></div>
        <p class="brand-name">Morvane Aesthetics</p>
      </div>
    </section>
    <section class="panel-front">
      <div class="brand">
        <div class="brand-dot"></div>
        <p class="brand-name">Morvane Aesthetics</p>
      </div>
      <p class="call-to-action">Call for appointment</p>
      <p class="phone">555-214-3870</p>
    </section>
  </main>
</body>
</html>
```